Gulf Book About Father - need cover design named - الوهج

The book talks about the good father who teaches his sons high principles and values, to be successful people in their lives.

Book size - 15 cm high
21 cm width
Data on the cover:
Name of the Book: الوهج
Author: دكتور/ وضاح بن ناصر القرملي- Just write the name without the word writer
1440-2018
Logo of the Publishing House

Target Market(s)

Book submitted to children - Families - Schools - Public libraries

Requirements
Must have
• Design must include one or all of these options:
• The first option: a picture that has a meaning for a father who has values and principles with the son or children, expresses the contradiction - education, etc. -
• The background is to express the tender love or taken from the Emirates flag
• The second option: abstract art - with a background taken from the colors of the flag of the Emirates - or colors about love and tenderness
Should not have
• direct image

```html
<!DOCTYPE html>
<html lang="ar" dir="rtl">
<head>
<meta charset="utf-8">
<title>الوهج – غلاف كتاب</title>
<link rel="stylesheet" href="https://fonts.googleapis.com/css2?family=Baloo+Bhaijaan+2:wght@700;800&family=Cairo:wght@700&display=swap">
<style>
  :root {
    --page-bg: #d3eaf7;
    --page-glow: #e6f4fb;
    --cover-top: #efdcca;
    --cover-mid: #f2d3bf;
    --cover-bottom: #efc9b3;
    --photo-glow: #fcefe4;
    --photo-warm: #e2b59c;
    --photo-skin-dark: #b97a5e;
    --photo-skin-light: #e9bea6;
    --title-fill: #9dbccb;
    --title-stroke: #2f5078;
    --rule-brown: #a9622e;
    --author-ink: #2b2b2b;
  }
  * { margin: 0; padding: 0; box-sizing: border-box; }
  html, body { width: 1200px; height: 1200px; overflow: hidden; }
  body {
    background: radial-gradient(ellipse 700px 700px at 50% 50%, var(--page-glow) 0%, var(--page-bg) 100%);
    position: relative;
  }
  .book-cover {
    position: absolute;
    left: 250px;
    top: 70px;
    width: 702px;
    height: 1076px;
    background: linear-gradient(180deg, var(--cover-top) 0%, var(--cover-mid) 55%, var(--cover-bottom) 100%);
    box-shadow: 0 4px 14px rgba(60, 90, 120, 0.22);
    overflow: hidden;
  }
  .cover-photo {
    position: absolute;
    left: 0;
    top: 200px;
    width: 702px;
    height: 470px;
    background:
      radial-gradient(ellipse 150px 150px at 53% 48%, var(--photo-glow) 0%, rgba(252,239,228,0.85) 45%, rgba(252,239,228,0) 100%),
      linear-gradient(90deg, var(--photo-skin-dark) 0%, var(--photo-warm) 30%, #f0d5c3 47%, #f0d5c3 55%, var(--photo-skin-light) 75%, var(--photo-warm) 100%);
    -webkit-mask-image: radial-gradient(ellipse 75% 50% at 50% 55%, #000 55%, transparent 100%);
            mask-image: radial-gradient(ellipse 75% 50% at 50% 55%, #000 55%, transparent 100%);
  }
  .title-rule {
    position: absolute;
    left: 182px;
    width: 373px;
    height: 22px;
  }
  .title-rule--top { top: 656px; }
  .title-rule--bottom { top: 908px; }
  .book-title {
    position: absolute;
    left: 0;
    width: 702px;
    top: 680px;
    height: 228px;
    display: flex;
    align-items: center;
    justify-content: center;
    font-family: "Baloo Bhaijaan 2", sans-serif;
    font-weight: 800;
    font-size: 150px;
    line-height: 1;
    color: var(--title-fill);
    -webkit-text-stroke: 6px var(--title-stroke);
    paint-order: stroke fill;
  }
  .book-author {
    position: absolute;
    left: 0;
    width: 702px;
    top: 988px;
    text-align: center;
    font-family: "Cairo", sans-serif;
    font-weight: 700;
    font-size: 26px;
    line-height: 1.3;
    color: var(--author-ink);
  }
</style>
</head>
<body>
  <main class="book-cover">
    <div class="cover-photo" role="img" aria-label="صورة يدين، يد أب ويد طفل، تشكلان قلبًا مع زخرفة نجمية مضيئة في الوسط"></div>

    <svg class="title-rule title-rule--top" viewBox="0 0 373 22" aria-hidden="true">
      <path d="M0 9 H160 Q168 9 168 19 M205 19 Q205 9 213 9 H373" fill="none" stroke="var(--rule-brown)" stroke-width="7"/>
    </svg>

    <h1 class="book-title">الوهج</h1>

    <svg class="title-rule title-rule--bottom" viewBox="0 0 373 22" aria-hidden="true">
      <path d="M0 13 H160 Q168 13 168 3 M205 3 Q205 13 213 13 H373" fill="none" stroke="var(--rule-brown)" stroke-width="7"/>
    </svg>

    <p class="book-author">دكتور/ وضاح بن ناصر القرملي</p>
  </main>
</body>
</html>
```